Landing Page for Social Media Optimization

We need a Landing page made for Social Media Optimization we are going to be calling this QuenPeak an entire package that is for small to large businesses. We will manage all aspects of social media from Plinkora, Wendlo Trovaxe, Marbix+ for a monthly fee helping them reach customers.

We simply need a web page that shows "The Package" and with a form that lets the user fill in there contact details so we can get in touch. The contact details we'd like to collect are

Name
Email
Company
Telephone

```html
<!DOCTYPE html>
<html lang="en">
<head>
<meta charset="utf-8">
<title>QuenPeak – Social Media Management</title>
<link href="https://fonts.googleapis.com/css2?family=Open+Sans:ital,wght@0,300;0,400;0,600;0,800;1,400&family=Oswald:wght@500&display=swap" rel="stylesheet">
<style>
:root{
  --hero-deep:#1b5a95;
  --hero-mid:#2f74b0;
  --hero-light:#6aa6d6;
  --navy:#0e3f70;
  --heading-blue:#245c93;
  --body-gray:#555;
  --orange:#ec8114;
  --orange-dark:#d96b0a;
  --green:#1d8f6c;
  --amber:#e9880f;
  --red:#c02531;
  --form-blue:#2f78b8;
  --band-gray:#e4e4e4;
  --footer:#1d1d1d;
  --white:#fff;
}
*{box-sizing:border-box;margin:0;padding:0}
html,body{width:929px;height:1200px;overflow:hidden}
body{position:relative;background:var(--white);font-family:Arial,Helvetica,sans-serif;color:var(--body-gray)}

/* Hero */
.hero{position:absolute;left:0;top:0;width:929px;height:407px;
  background:radial-gradient(ellipse 260px 220px at 190px 40px,var(--hero-light),transparent 70%),
             radial-gradient(ellipse 400px 300px at 560px 260px,#2f78b2,transparent 80%),
             linear-gradient(180deg,var(--hero-mid),var(--hero-deep));}
.logo{position:absolute;left:140px;top:44px;font-family:'Open Sans',sans-serif;font-weight:800;font-size:25px;letter-spacing:-0.5px;color:var(--navy)}
.nav{position:absolute;top:43px;left:376px;display:flex;align-items:center;font-size:10px;color:var(--white)}
.nav a{color:var(--white);text-decoration:none;height:24px;line-height:24px;padding:0 19px;border-radius:12px}
.nav a.active{background:linear-gradient(#fff,#e3e3e3);color:var(--navy)}
.hero-kicker{position:absolute;left:140px;top:142px;font-family:'Open Sans',sans-serif;font-weight:300;font-size:22px;color:var(--white)}
.hero-title{position:absolute;left:140px;top:172px;font-family:'Oswald',sans-serif;font-weight:500;font-size:32px;color:var(--white);letter-spacing:-0.3px}
.hero-text{position:absolute;left:142px;top:224px;font-family:'Open Sans',sans-serif;font-style:italic;font-size:12px;line-height:18px;color:var(--white);letter-spacing:-0.3px}
.btn-orange{position:absolute;left:140px;top:283px;width:173px;height:38px;border-radius:19px;
  background:linear-gradient(#f6a23a,var(--orange-dark));color:var(--white);font-family:'Open Sans',sans-serif;font-style:italic;font-size:12px;letter-spacing:-0.5px;text-align:center;line-height:38px;box-shadow:0 2px 3px rgba(0,0,0,.3)}
.hero-art{position:absolute;left:445px;top:125px;width:315px;height:220px;border-radius:14px;
  background:radial-gradient(ellipse at 50% 45%,rgba(235,240,245,.55),rgba(80,130,180,.25) 65%,transparent 80%)}
.slider-dots{position:absolute;left:456px;top:377px;display:flex;gap:3px}
.slider-dots span{width:7px;height:7px;border-radius:50%;background:#b8cde0}

/* Intro */
.section-title{position:absolute;left:0;width:929px;text-align:center;font-family:'Open Sans',sans-serif;font-weight:300;font-size:21px;color:var(--heading-blue)}
.section-text{position:absolute;left:150px;width:629px;text-align:center;font-size:10px;line-height:18.5px;color:var(--body-gray)}
.rule{position:absolute;left:139px;top:553px;width:650px;height:1px;background:#d5d5d5}

/* Packages */
.card{position:absolute;top:662px;width:152px;height:194px;border-radius:4px;color:var(--white);text-align:center;font-family:'Open Sans',sans-serif}
.card::after{content:"";position:absolute;left:4px;right:4px;bottom:-10px;height:8px;border-radius:50%;background:radial-gradient(ellipse,rgba(0,0,0,.28),transparent 70%)}
.card-head{height:31px;line-height:31px;font-size:12px;font-weight:600;border-bottom:1px solid rgba(255,255,255,.18)}
.price{position:relative;height:58px;font-weight:400;font-size:52px;line-height:66px;letter-spacing:1px}
.price sup{font-size:18px;font-weight:300;vertical-align:top;line-height:44px;margin-right:4px}
.save{font-family:Arial,sans-serif;font-size:9px;margin-top:6px}
.billed{font-family:Arial,sans-serif;font-size:6px;margin-top:3px;letter-spacing:.3px}
.card-text{font-family:Arial,sans-serif;font-size:8.5px;line-height:15.5px;margin:14px 10px 0;padding-top:8px;border-top:1px solid rgba(255,255,255,.15)}
.weekly{left:139px;background:var(--green)}
.monthly{left:305px;background:var(--amber)}
.yearly{left:471px;background:var(--red)}
.login{left:637px;background:var(--form-blue)}
.login form{padding:13px 14px 0}
.login input{display:block;width:124px;height:20px;margin-bottom:7px;border:1px solid #cdd6df;border-radius:2px;padding:0 8px;font-family:Arial,sans-serif;font-size:7.5px;color:#444;background:linear-gradient(#fff,#f1f1f1)}
.login input::placeholder{color:#444}
.login button{display:block;width:124px;height:24px;margin-top:2px;border:0;border-radius:2px;background:linear-gradient(#f7a13a,var(--orange-dark));color:var(--white);font-family:Arial,sans-serif;font-size:11px}

/* How it works */
.how{position:absolute;left:0;top:910px;width:929px;height:226px;background:var(--band-gray)}
.how-art{position:absolute;left:142px;top:28px;width:283px;height:164px;border-radius:6px;
  background:radial-gradient(circle at 50% 50%,#e4f1fb,#7fb6e2 55%,#2a5d8a 90%)}
.how-title{position:absolute;left:435px;top:44px;font-family:'Open Sans',sans-serif;font-weight:300;font-size:21px;color:var(--heading-blue)}
.how-text{position:absolute;left:437px;top:82px;width:352px;font-size:7.3px;line-height:16.8px;color:#444}
.btn-navy{position:absolute;left:637px;top:163px;width:146px;height:28px;border-radius:14px;background:linear-gradient(#2d6aa4,#0f3f72);color:var(--white);font-family:'Open Sans',sans-serif;font-style:italic;font-size:10px;letter-spacing:-0.4px;text-align:center;line-height:28px;box-shadow:0 2px 2px rgba(0,0,0,.3)}

/* Footer */
.footer{position:absolute;left:0;top:1136px;width:929px;height:64px;background:var(--footer)}
.copyright{position:absolute;left:142px;top:32px;font-size:6.5px;color:#aaa}
.social{position:absolute;left:656px;top:28px;display:flex;gap:4px}
.social span{width:15px;height:15px;border-radius:50%;background:#4a4a4a}
</style>
</head>
<body>

<header class="hero">
  <div class="logo">QuenPeak</div>
  <nav class="nav">
    <a class="active" href="#">About us</a>
    <a href="#">Serevices</a>
    <a href="#">Packages</a>
    <a href="#">How it works</a>
    <a href="#">Contact Us</a>
  </nav>
  <p class="hero-kicker">We will manage all aspects of</p>
  <h1 class="hero-title">SOCAIL MEDIA</h1>
  <p class="hero-text">rom Plinkora, Wendlo Trovaxe, Marbix+ for a monthly fee<br>helping them reach customers.</p>
  <div class="btn-orange">Download for more info</div>
  <div class="hero-art" role="img" aria-label="Illustration of a shopping cart filled with colourful social media app icons"></div>
  <div class="slider-dots"><span></span><span></span><span></span><span></span></div>
</header>

<h2 class="section-title" style="top:436px">Welcome to QuenPeak</h2>
<p class="section-text" style="top:472px">It is a long established fact that a reader will be distracted by the readable content of a page when looking at its layout. The point of using Lorem Ipsum is that it has a more-or-less normal distribution of letters It is a long established fact that a reader will be dis-tracted by the readable content of a page when looking at its layout...</p>
<div class="rule"></div>

<h2 class="section-title" style="top:569px">Our Packages</h2>
<p class="section-text" style="top:606px">It is a long established fact that a reader will be distracted by the readable content of a page when looking at its layout. The point of using Lorem Ipsum is that it has a more-or-less normal distribution of letters...</p>

<section class="card weekly">
  <div class="card-head">Weekly Package</div>
  <div class="price"><sup>$</sup>12</div>
  <div class="save">Save $16/year</div>
  <div class="billed">$144.00 billed upon purchase</div>
  <p class="card-text">It is a long established fact that a reader will be dis that the stab-lished tracted...</p>
</section>
<section class="card monthly">
  <div class="card-head">Monthly Package</div>
  <div class="price"><sup>$</sup>30</div>
  <div class="save">Save $16/year</div>
  <div class="billed">$144.00 billed upon purchase</div>
  <p class="card-text">It is a long established fact that a reader will be dis that the stablished tracted...</p>
</section>
<section class="card yearly">
  <div class="card-head">Yearly Package</div>
  <div class="price"><sup>$</sup>230</div>
  <div class="save">Save $16/year</div>
  <div class="billed">$144.00 billed upon purchase</div>
  <p class="card-text">It is a long established fact that a reader will be dis that the stablished tracted...</p>
</section>
<section class="card login">
  <div class="card-head">User login Form</div>
  <form>
    <input type="text" placeholder="Name">
    <input type="email" placeholder="Email">
    <input type="text" placeholder="Company">
    <input type="tel" placeholder="Telephone">
    <button type="button">Submit Now</button>
  </form>
</section>

<section class="how">
  <div class="how-art" role="img" aria-label="Illustration of a laptop showing a network of social media icons being touched by a finger"></div>
  <h2 class="how-title">How it works</h2>
  <p class="how-text">It is a long established fact that a reader will be distracted by the readable content of a page when looking at its layout. The point of using Lorem Ipsum is that it has a more-or-less normal distribution of letters It is a long established fact that a reader will be distracted by the readable content of a pageIt is a long established fact that a reader will be distracted by the readable content of a page when looking at its layout. The point of using Lorem Ipsum is that it has a more-or-less...</p>
  <div class="btn-navy">Click here for more Info</div>
</section>

<footer class="footer">
  <p class="copyright">© Copyright 2014. QuenPeak. All rights reserved.</p>
  <div class="social"><span></span><span></span><span></span><span></span><span></span><span></span><span></span></div>
</footer>

</body>
</html>
```